Waterjet manufacturing company needs brochure design

We need a brochure that outlines why waterjet manufacturing is beneficial for a variety of industries, our capabilities, core competencies and competitive advantages (see attached documents). The design should include our logo and include the same colours. (Dark blue RGB – 2,86,162, Light Blue RGB – 0,146,201). The design should be very clean, professional and eye catching. I've attached a few photos that can be used. Regarding the photo of the robot, please make the background white.

Manufacturing, construction, aerospace, home building

• - exact Logo colours included in design (see description)
• - booklet style design (not tri-fold)
• - professional looking
• - Logo on front cover with writing underneath:
• High Quality
• Tight Tolerance
• Components
• - Plankrow, Ropelane, Vidstow and Pixelmorra icons in Contact Us section

```html
<!DOCTYPE html>
<html lang="en">
<head>
<meta charset="utf-8">
<title>Northvale Waterjet Brochure</title>
<link rel="stylesheet" href="https://fonts.googleapis.com/css2?family=Montserrat:wght@400;600;700;800&family=Open+Sans:wght@400;600&display=swap">
<style>
:root{
  --dark-blue:#0256a2;
  --light-blue:#0092c9;
  --navy:#0b2e5a;
  --ink:#1d2733;
  --muted:#5d6a78;
  --paper:#ffffff;
  --stage-top:#bdbdbd;
  --stage-bottom:#e9e9e9;
}
*{box-sizing:border-box;margin:0;padding:0}
html,body{width:1200px;height:2476px;overflow:hidden}
body{font-family:"Open Sans",Arial,sans-serif;color:var(--ink);background:var(--stage-bottom);position:relative}
.stage-top{position:absolute;left:0;top:0;width:1200px;height:880px;background:var(--stage-top)}
.page{position:relative;width:540px;height:380px;overflow:hidden;background:var(--paper)}
.page .bg{position:absolute;inset:0;width:100%;height:100%}
.cover-single{position:absolute;transform-origin:0 0;transform:scale(.95);box-shadow:0 14px 30px rgba(0,0,0,.28)}
.spread{position:absolute;left:60px;width:1080px;height:380px;display:flex;box-shadow:0 12px 28px rgba(0,0,0,.22)}
h2,h3,.brand{font-family:"Montserrat",Arial,sans-serif}

/* front cover */
.brand{position:absolute;left:40px;top:78px;color:#fff}
.brand-name{font-size:28px;font-weight:700;line-height:1.1;color:#fff}
.tagline{font-size:18px;font-weight:600;margin-top:14px}
.cover-web{position:absolute;right:26px;bottom:58px;color:#fff;font-size:8px;letter-spacing:1.5px;font-family:"Montserrat",sans-serif}

/* back cover */
.contact{position:absolute;left:318px;top:56px;width:200px;color:#fff}
.contact h2{font-size:22px;font-weight:700}
.contact .lead{font-size:8.5px;margin:4px 0 16px;line-height:1.5}
.contact ul{list-style:none}
.contact li{display:flex;align-items:center;gap:8px;font-size:8.5px;margin-bottom:9px}
.contact li svg{width:12px;height:12px;flex:none}
.socials{display:flex;flex-wrap:wrap;gap:6px 12px;margin-top:12px}
.socials span{display:flex;align-items:center;gap:4px;font-size:7.5px}
.socials i{width:9px;height:9px;border-radius:50%;background:#fff;display:block}

/* why choose */
.why{position:absolute;right:30px;top:34px;width:330px;text-align:right}
.why h2{font-size:20px;font-weight:700;color:var(--ink);line-height:1.1}
.why h2 span{display:block;color:var(--dark-blue);font-size:19px}
.why .rule{width:60px;height:3px;background:var(--light-blue);margin:10px 0 12px auto}
.why p{font-size:7.6px;line-height:1.6;color:var(--muted);margin-bottom:8px}
.foot-note{position:absolute;bottom:18px;font-size:7.5px;color:var(--muted);font-family:"Montserrat",sans-serif;letter-spacing:.5px}

/* benefits */
.benefits{position:absolute;left:28px;top:30px;width:400px;color:#fff}
.benefits h2{font-size:17px;font-weight:700;line-height:1.2}
.benefits h2 span{display:block;font-size:15px;color:#bfe7f7}
.benefits .rule{width:60px;height:3px;background:var(--light-blue);margin:10px 0 14px}
.benefit-cols{display:grid;grid-template-columns:1fr 1fr;gap:10px 20px}
.benefit h3{font-size:9px;font-weight:700;display:flex;align-items:center;gap:5px}
.benefit h3 svg{width:10px;height:10px;flex:none}
.benefit p{font-size:7px;line-height:1.5;color:#dbe9f6;margin-top:2px}
.white-web{color:#fff}

/* comparison */
.compare{position:absolute;left:28px;top:30px;width:480px}
.compare h2{font-size:17px;font-weight:700;color:var(--dark-blue)}
.compare .rule{height:2px;background:var(--light-blue);margin:8px 0 14px}
.compare table{width:100%;border-collapse:separate;border-spacing:3px;font-size:7px}
.compare th{background:var(--dark-blue);color:#fff;font-family:"Montserrat",sans-serif;font-size:7.5px;padding:5px 3px;font-weight:700}
.compare th.blank{background:none}
.compare td{background:#eef3f8;padding:6px 4px;text-align:center;color:var(--muted);line-height:1.35}
.compare td.row{background:none;color:var(--dark-blue);font-weight:700;font-family:"Montserrat",sans-serif;text-align:left;font-size:7.5px}

/* materials */
.materials{position:absolute;left:28px;top:30px;width:340px}
.materials h2{font-size:18px;font-weight:700;color:var(--navy)}
.materials .rule{width:60px;height:3px;background:var(--light-blue);margin:8px 0 12px}
.material{margin-bottom:8px}
.material h3{font-size:8.5px;font-weight:700;color:var(--dark-blue)}
.material h3 b{color:var(--light-blue);margin-right:5px}
.material p{font-size:7px;line-height:1.45;color:var(--muted)}
</style>
</head>
<body>

<div class="stage-top"></div>

<div class="cover-single" style="left:60px;top:250px">
  <section class="page front-cover">
    <svg class="bg" viewBox="0 0 540 380">
      <defs>
        <linearGradient id="navyA" x1="0" y1="0" x2="1" y2="1"><stop offset="0" stop-color="#0b2e5a"/><stop offset="1" stop-color="#0256a2"/></linearGradient>
        <linearGradient id="jetA" x1="0" y1="0" x2="1" y2="1"><stop offset="0" stop-color="#c9cdd2"/><stop offset=".55" stop-color="#7d7a6f"/><stop offset="1" stop-color="#2f3d4c"/></linearGradient>
      </defs>
      <rect width="540" height="380" fill="url(#navyA)"/>
      <g role="img" aria-label="Waterjet cutting head spraying onto a metal plate"><polygon points="260,0 540,0 540,275 340,275" fill="url(#jetA)"/></g>
      <polygon points="0,300 540,250 540,292 0,342" fill="#0092c9"/>
      <polygon points="0,342 540,292 540,380 0,380" fill="#0b2e5a"/>
    </svg>
    <div class="brand">
      <div class="brand-name">Northvale Waterjet</div>
      <div class="tagline">We make the cut!</div>
    </div>
    <div class="cover-web">www.northvalewaterjet.com</div>
  </section>
</div>

<div class="cover-single" style="left:627px;top:250px">
  <section class="page back-cover">
    <svg class="bg" viewBox="0 0 540 380">
      <defs>
        <linearGradient id="steelA" x1="0" y1="0" x2="1" y2="1"><stop offset="0" stop-color="#b9c4cf"/><stop offset="1" stop-color="#4f5f70"/></linearGradient>
      </defs>
      <g role="img" aria-label="Close-up of precision waterjet-cut metal parts"><polygon points="0,0 330,0 250,380 0,380" fill="url(#steelA)"/></g>
      <polygon points="330,0 540,0 540,380 250,380" fill="#0256a2"/>
      <polygon points="316,0 334,0 254,380 236,380" fill="#0092c9"/>
      <polygon points="250,380 540,380 540,352 256,352" fill="#0b2e5a"/>
    </svg>
    <div class="contact">
      <h2>Contact Us</h2>
      <p class="lead">Got a need for a part?<br>Give us a call today!</p>
      <ul>
        <li><svg viewBox="0 0 12 12"><path d="M3 1l2 2-1 1.5c.8 1.6 1.9 2.7 3.5 3.5L9 7l2 2-1.5 2C5 10.5 1.5 7 1 2.5z" fill="#fff"/></svg>905-555-0142</li>
        <li><svg viewBox="0 0 12 12"><rect x="1" y="2.5" width="10" height="7" fill="none" stroke="#fff"/><path d="M1 2.5l5 4 5-4" fill="none" stroke="#fff"/></svg>info@northvalewaterjet.com</li>
        <li><svg viewBox="0 0 12 12"><circle cx="6" cy="6" r="4.8" fill="none" stroke="#fff"/><path d="M1.2 6h9.6M6 1.2c-2.4 3-2.4 6.6 0 9.6M6 1.2c2.4 3 2.4 6.6 0 9.6" fill="none" stroke="#fff" stroke-width=".8"/></svg>www.northvalewaterjet.com</li>
        <li><svg viewBox="0 0 12 12"><path d="M6 11S2 7 2 4.5a4 4 0 018 0C10 7 6 11 6 11z" fill="#fff"/><circle cx="6" cy="4.5" r="1.4" fill="#0256a2"/></svg>214 Harbour Road, Vale ON</li>
      </ul>
      <div class="socials"><span><i></i>Plankrow</span><span><i></i>Ropelane</span><span><i></i>Vidstow</span><span><i></i>Pixelmorra</span></div>
    </div>
  </section>
</div>

<div class="spread" style="top:950px">
  <section class="page back-cover">
    <svg class="bg" viewBox="0 0 540 380">
      <defs>
        <linearGradient id="steelB" x1="0" y1="0" x2="1" y2="1"><stop offset="0" stop-color="#b9c4cf"/><stop offset="1" stop-color="#4f5f70"/></linearGradient>
      </defs>
      <g role="img" aria-label="Close-up of precision waterjet-cut metal parts"><polygon points="0,0 330,0 250,380 0,380" fill="url(#steelB)"/></g>
      <polygon points="330,0 540,0 540,380 250,380" fill="#0256a2"/>
      <polygon points="316,0 334,0 254,380 236,380" fill="#0092c9"/>
      <polygon points="250,380 540,380 540,352 256,352" fill="#0b2e5a"/>
    </svg>
    <div class="contact">
      <h2>Contact Us</h2>
      <p class="lead">Got a need for a part?<br>Give us a call today!</p>
      <ul>
        <li><svg viewBox="0 0 12 12"><path d="M3 1l2 2-1 1.5c.8 1.6 1.9 2.7 3.5 3.5L9 7l2 2-1.5 2C5 10.5 1.5 7 1 2.5z" fill="#fff"/></svg>905-555-0142</li>
        <li><svg viewBox="0 0 12 12"><rect x="1" y="2.5" width="10" height="7" fill="none" stroke="#fff"/><path d="M1 2.5l5 4 5-4" fill="none" stroke="#fff"/></svg>info@northvalewaterjet.com</li>
        <li><svg viewBox="0 0 12 12"><circle cx="6" cy="6" r="4.8" fill="none" stroke="#fff"/><path d="M1.2 6h9.6M6 1.2c-2.4 3-2.4 6.6 0 9.6M6 1.2c2.4 3 2.4 6.6 0 9.6" fill="none" stroke="#fff" stroke-width=".8"/></svg>www.northvalewaterjet.com</li>
        <li><svg viewBox="0 0 12 12"><path d="M6 11S2 7 2 4.5a4 4 0 018 0C10 7 6 11 6 11z" fill="#fff"/><circle cx="6" cy="4.5" r="1.4" fill="#0256a2"/></svg>214 Harbour Road, Vale ON</li>
      </ul>
      <div class="socials"><span><i></i>Plankrow</span><span><i></i>Ropelane</span><span><i></i>Vidstow</span><span><i></i>Pixelmorra</span></div>
    </div>
  </section>
  <section class="page front-cover">
    <svg class="bg" viewBox="0 0 540 380">
      <defs>
        <linearGradient id="navyB" x1="0" y1="0" x2="1" y2="1"><stop offset="0" stop-color="#0b2e5a"/><stop offset="1" stop-color="#0256a2"/></linearGradient>
        <linearGradient id="jetB" x1="0" y1="0" x2="1" y2="1"><stop offset="0" stop-color="#c9cdd2"/><stop offset=".55" stop-color="#7d7a6f"/><stop offset="1" stop-color="#2f3d4c"/></linearGradient>
      </defs>
      <rect width="540" height="380" fill="url(#navyB)"/>
      <g role="img" aria-label="Waterjet cutting head spraying onto a metal plate"><polygon points="260,0 540,0 540,275 340,275" fill="url(#jetB)"/></g>
      <polygon points="0,300 540,250 540,292 0,342" fill="#0092c9"/>
      <polygon points="0,342 540,292 540,380 0,380" fill="#0b2e5a"/>
    </svg>
    <div class="brand">
      <div class="brand-name">Northvale Waterjet</div>
      <div class="tagline">We make the cut!</div>
    </div>
    <div class="cover-web">www.northvalewaterjet.com</div>
  </section>
</div>

<div class="spread" style="top:1420px">
  <section class="page why-page">
    <svg class="bg" viewBox="0 0 540 380">
      <defs>
        <linearGradient id="glow" x1="0" y1="0" x2="0" y2="1"><stop offset="0" stop-color="#0b2e5a"/><stop offset=".6" stop-color="#0092c9"/><stop offset="1" stop-color="#0b2e5a"/></linearGradient>
      </defs>
      <g role="img" aria-label="Waterjet nozzle with blue-lit cutting stream"><polygon points="0,0 160,0 95,380 0,380" fill="url(#glow)"/></g>
      <polygon points="160,0 174,0 109,380 95,380" fill="#0092c9"/>
      <polygon points="178,0 183,0 118,380 113,380" fill="#0256a2"/>
    </svg>
    <div class="why">
      <h2>Why Choose <span>NORTHVALE WATERJET?</span></h2>
      <div class="rule"></div>
      <p>For over two decades our team has delivered precise, dependable parts to manufacturers across the region. We pair modern waterjet systems with skilled operators to turn your drawings into finished components quickly.</p>
      <p>Our shop handles single prototypes and full production runs alike, holding tight tolerances on metals, stone, glass, composites and plastics without heat damage or secondary finishing.</p>
      <p>From aerospace and construction to home building, customers rely on our fast quotes, honest pricing and on-time delivery. Every job is inspected before it leaves our floor.</p>
    </div>
    <div class="foot-note" style="left:130px">info@northvalewaterjet.com</div>
  </section>
  <section class="page benefits-page">
    <svg class="bg" viewBox="0 0 540 380">
      <defs>
        <linearGradient id="blueBg" x1="0" y1="0" x2="1" y2="1"><stop offset="0" stop-color="#0256a2"/><stop offset="1" stop-color="#0b2e5a"/></linearGradient>
        <linearGradient id="steelC" x1="0" y1="0" x2="0" y2="1"><stop offset="0" stop-color="#9aa8b6"/><stop offset="1" stop-color="#3c4b5a"/></linearGradient>
      </defs>
      <rect width="540" height="380" fill="url(#blueBg)"/>
      <polygon points="452,0 470,0 410,380 392,380" fill="#0092c9"/>
      <g role="img" aria-label="Waterjet machine cutting a thick steel part"><polygon points="474,0 540,0 540,380 414,380" fill="url(#steelC)"/></g>
    </svg>
    <div class="benefits">
      <h2>Benefits of Waterjet Cutting with <span>NORTHVALE WATERJET</span></h2>
      <div class="rule"></div>
      <div class="benefit-cols">
        <div class="benefit"><h3><svg viewBox="0 0 10 10"><path d="M1.5 5l2.5 2.5L8.5 2" fill="none" stroke="#0092c9" stroke-width="1.8"/></svg>Versatility</h3><p>Cuts almost any material and thickness on one machine.</p></div>
        <div class="benefit"><h3><svg viewBox="0 0 10 10"><path d="M1.5 5l2.5 2.5L8.5 2" fill="none" stroke="#0092c9" stroke-width="1.8"/></svg>Cost Effectiveness</h3><p>Less setup and tooling keeps part prices low.</p></div>
        <div class="benefit"><h3><svg viewBox="0 0 10 10"><path d="M1.5 5l2.5 2.5L8.5 2" fill="none" stroke="#0092c9" stroke-width="1.8"/></svg>Precision</h3><p>Tight tolerances held on detailed shapes.</p></div>
        <div class="benefit"><h3><svg viewBox="0 0 10 10"><path d="M1.5 5l2.5 2.5L8.5 2" fill="none" stroke="#0092c9" stroke-width="1.8"/></svg>No Heat Distortion</h3><p>Cold cutting leaves no hardened edges.</p></div>
        <div class="benefit"><h3><svg viewBox="0 0 10 10"><path d="M1.5 5l2.5 2.5L8.5 2" fill="none" stroke="#0092c9" stroke-width="1.8"/></svg>Speed</h3><p>Fast turnaround from file to finished part.</p></div>
        <div class="benefit"><h3><svg viewBox="0 0 10 10"><path d="M1.5 5l2.5 2.5L8.5 2" fill="none" stroke="#0092c9" stroke-width="1.8"/></svg>Smooth Edges</h3><p>Clean cuts that rarely need finishing.</p></div>
        <div class="benefit"><h3><svg viewBox="0 0 10 10"><path d="M1.5 5l2.5 2.5L8.5 2" fill="none" stroke="#0092c9" stroke-width="1.8"/></svg>Reduced Waste</h3><p>Narrow kerf and nesting save material.</p></div>
        <div class="benefit"><h3><svg viewBox="0 0 10 10"><path d="M1.5 5l2.5 2.5L8.5 2" fill="none" stroke="#0092c9" stroke-width="1.8"/></svg>Eco Friendly</h3><p>No fumes or hazardous by-products.</p></div>
      </div>
    </div>
    <div class="foot-note white-web" style="left:28px">www.northvalewaterjet.com</div>
  </section>
</div>

<div class="spread" style="top:1890px">
  <section class="page compare-page">
    <div class="compare">
      <h2>Comparative Cutting Technologies</h2>
      <div class="rule"></div>
      <table>
        <tr><th class="blank"></th><th>Waterjet</th><th>Laser</th><th>Plasma</th><th>EDM</th></tr>
        <tr><td class="row">Precision</td><td>High, ±0.003"</td><td>High</td><td>Moderate</td><td>Very high</td></tr>
        <tr><td class="row">Edge Quality</td><td>Smooth, no burr</td><td>Good</td><td>Rough edge</td><td>Excellent</td></tr>
        <tr><td class="row">Material Range</td><td>Nearly all materials</td><td>Metals, some plastics</td><td>Conductive metals</td><td>Conductive only</td></tr>
        <tr><td class="row">Heat Zone</td><td>None</td><td>Small</td><td>Large</td><td>Small</td></tr>
        <tr><td class="row">Thickness</td><td>Up to 8"</td><td>Up to 1"</td><td>Up to 2"</td><td>Up to 12"</td></tr>
        <tr><td class="row">Setup Time</td><td>Minimal</td><td>Minimal</td><td>Minimal</td><td>Long</td></tr>
      </table>
    </div>
    <div class="foot-note" style="left:28px">www.northvalewaterjet.com</div>
  </section>
  <section class="page materials-page">
    <svg class="bg" viewBox="0 0 540 380">
      <defs>
        <linearGradient id="softBg" x1="0" y1="0" x2="1" y2="1"><stop offset="0" stop-color="#f4f7fa"/><stop offset="1" stop-color="#d5dee7"/></linearGradient>
        <linearGradient id="steelD" x1="0" y1="0" x2="0" y2="1"><stop offset="0" stop-color="#aab5c0"/><stop offset="1" stop-color="#4a5968"/></linearGradient>
      </defs>
      <g role="img" aria-label="Faint background of waterjet-cut material samples"><rect width="540" height="380" fill="url(#softBg)"/></g>
      <polygon points="430,0 470,0 400,380 360,380" fill="#0256a2"/>
      <polygon points="472,0 480,0 410,380 402,380" fill="#0092c9"/>
      <g role="img" aria-label="Robot arm handling a cut part on a white background"><polygon points="484,0 540,0 540,380 414,380" fill="url(#steelD)"/></g>
    </svg>
    <div class="materials">
      <h2>Materials We Cut</h2>
      <div class="rule"></div>
      <div class="material"><h3><b>01</b>METALS</h3><p>Steel, stainless, aluminum, titanium, brass and copper.</p></div>
      <div class="material"><h3><b>02</b>COMPOSITES</h3><p>Carbon fibre, fibreglass and laminated panels.</p></div>
      <div class="material"><h3><b>03</b>STONE &amp; TILE</h3><p>Granite, marble, porcelain and ceramic inlays.</p></div>
      <div class="material"><h3><b>04</b>GLASS</h3><p>Flat, laminated and decorative glass pieces.</p></div>
      <div class="material"><h3><b>05</b>PLASTICS, RUBBER &amp; FOAM</h3><p>Acrylic, nylon, gaskets, seals and packaging foam.</p></div>
      <div class="material"><h3><b>06</b>WOOD &amp; SPECIALTY</h3><p>Hardwood, plywood and custom sheet materials.</p></div>
    </div>
    <div class="foot-note" style="left:28px">www.northvalewaterjet.com</div>
  </section>
</div>

</body>
</html>
```